Concert festival poster

Poster invitation for 40th party designed to look like a concert festival. Using the samples attached as a guide, looking for a colorful, creative and eye catching invite.
The event will be held over a weekend at a farm, with music food, friends and drinks.

Target Market(s)

Party guests, friends and family

Industry/Entity Type

Festival

Colors

Designer to choose colors to be used in the design.

Requirements
Must have
• Brellafest- Mark Telford's 40th festival
• Event date- 5-7th October 2018. Main event 6th October 2018 from 3pm-late
• Come anytime over the weekend- food, drinks and fun provided.
• Address is 412 Stony Creek Lane, Brindlevale NSW
• All welcome, including children
• Bring your own tent or let us know and we can arrange glamping tent set-up on site
• RSVP by 1 May 2018 to Kate at kate.anne.telford@mailbox-demo.com or Mark at mtelford@vantor-telford.com.au
• Will add extra information on event at later stage- see below for editable section.
Nice to have
• Editable section to add details, preferable at bottom of poster.

```html
<!DOCTYPE html>
<html lang="en">
<head>
<meta charset="utf-8">
<title>Brellafest – Mark Telford's 40th Festival</title>
<link href="https://fonts.googleapis.com/css2?family=Montserrat:wght@400;600;700&family=Oswald:wght@500;600&family=Questrial&family=Righteous&display=swap" rel="stylesheet">
<style>
  :root {
    --backdrop: #e9e9e9;
    --poster: #1e1a16;
    --ink: #ffffff;
    --ink-soft: #e8e4df;
    --rule: #5a5550;
    --red: #ec2a3a;
    --orange: #f7941d;
    --yellow: #f9c52b;
    --teal: #1aa6a8;
    --purple: #7b3f98;
    --pin: #2bb3b1;
    --mail: #e0404a;
  }
  * { margin: 0; padding: 0; box-sizing: border-box; }
  html, body { width: 1200px; height: 900px; overflow: hidden; }
  body {
    background: var(--backdrop);
    font-family: "Questrial", "Century Gothic", sans-serif;
    color: var(--ink);
    position: relative;
  }
  .poster {
    position: absolute;
    left: 291px; top: 20px;
    width: 618px; height: 860px;
    background: var(--poster);
    overflow: hidden;
  }
  .artwork {
    position: absolute;
    left: 320px; top: 0;
    width: 298px; height: 860px;
    background: linear-gradient(180deg, var(--teal) 0%, var(--yellow) 10%, var(--orange) 28%, var(--yellow) 40%, var(--orange) 52%, var(--purple) 62%, var(--teal) 72%, var(--red) 84%, var(--orange) 92%, var(--yellow) 100%);
    clip-path: polygon(210px 35px, 298px 35px, 298px 860px, 150px 860px, 160px 800px, 60px 765px, 50px 720px, 90px 700px, 40px 690px, 40px 660px, 120px 650px, 35px 620px, 30px 590px, 160px 580px, 150px 520px, 60px 545px, 70px 470px, 160px 460px, 185px 400px, 210px 360px, 200px 260px, 130px 260px, 130px 145px, 240px 140px, 240px 110px, 10px 105px, 0 65px, 230px 60px);
    opacity: 0.95;
  }
  .block { position: absolute; left: 35px; white-space: nowrap; }
  .host { top: 32px; font-family: "Questrial", sans-serif; font-size: 26px; letter-spacing: 0.3px; }
  .occasion { top: 54px; font-family: "Oswald", sans-serif; font-weight: 600; font-size: 38px; letter-spacing: 0.6px; }
  .festival-name {
    top: 104px;
    font-family: "Righteous", sans-serif;
    font-size: 86px; line-height: 78px;
    background: linear-gradient(100deg, var(--red) 0%, var(--teal) 30%, var(--orange) 55%, var(--yellow) 75%, var(--teal) 100%);
    -webkit-background-clip: text; background-clip: text;
    color: transparent;
  }
  .divider { position: absolute; left: 0; top: 286px; width: 420px; height: 2px; background: var(--rule); }
  .label { font-family: "Oswald", sans-serif; font-weight: 500; font-size: 20px; letter-spacing: 0.4px; }
  .date-label { top: 305px; }
  .date { top: 338px; font-size: 26px; }
  .date sup { font-size: 13px; }
  .main-event { top: 376px; font-family: "Montserrat", sans-serif; font-weight: 600; font-size: 11px; }
  .main-event sup { font-size: 7px; }
  .weekend { top: 414px; font-size: 16.5px; line-height: 17px; }
  .address-label { top: 484px; }
  .address { top: 520px; font-size: 15.5px; display: flex; align-items: center; gap: 7px; }
  .welcome-label { top: 570px; }
  .welcome { top: 597px; font-size: 22px; }
  .tent { top: 645px; font-family: "Montserrat", sans-serif; font-weight: 600; font-size: 19px; }
  .tent-note { top: 671px; font-size: 11px; line-height: 13px; color: var(--ink-soft); }
  .rsvp { top: 728px; font-size: 21px; }
  .rsvp small, .rsvp-date small { font-family: "Montserrat", sans-serif; font-size: 11px; font-weight: 600; margin-left: 6px; letter-spacing: 0; }
  .rsvp-date { top: 760px; font-family: "Oswald", sans-serif; font-weight: 500; font-size: 23px; letter-spacing: 0.5px; }
  .contact { font-family: "Montserrat", sans-serif; font-weight: 600; font-size: 12px; display: flex; align-items: center; gap: 8px; }
  .contact-one { top: 795px; }
  .contact-two { top: 814px; }
</style>
</head>
<body>
  <main class="poster">
    <div class="artwork" role="img" aria-label="Colourful faceted illustration of stacked musical instruments: guitars, keyboard, trumpets, speaker and saxophone"></div>

    <p class="block host">MARK TELFORD'S</p>
    <h2 class="block occasion">40TH FESTIVAL</h2>
    <h1 class="block festival-name">BRELLA<br>FEST</h1>
    <div class="divider"></div>

    <h3 class="block label date-label">EVENT DATE</h3>
    <p class="block date">5-7<sup>TH</sup> OCTOBER 2018</p>
    <p class="block main-event">Main event 6<sup>th</sup> October 2018 from 3pm-late</p>
    <p class="block weekend">Come anytime over the weekend<br>Food, drinks and fun provided</p>

    <h3 class="block label address-label">ADDRESS</h3>
    <p class="block address">
      <svg width="8" height="11" viewBox="0 0 8 11" aria-hidden="true"><path d="M4 0a4 4 0 0 0-4 4c0 3 4 7 4 7s4-4 4-7a4 4 0 0 0-4-4z" fill="var(--pin)"/><circle cx="4" cy="4" r="1.5" fill="var(--poster)"/></svg>
      412 Stony Creek Lane, Brindlevale NSW
    </p>

    <h3 class="block label welcome-label">ALL WELCOME</h3>
    <p class="block welcome">Including children</p>

    <p class="block tent">Bring your own tent</p>
    <p class="block tent-note">or let us know and we can arrange<br>glamping tent set-up on site</p>

    <p class="block label rsvp">RSVP<small>by</small></p>
    <p class="block rsvp-date">1 MAY 2018<small>to</small></p>
    <p class="block contact contact-one">
      <svg width="8" height="6" viewBox="0 0 8 6" aria-hidden="true"><rect width="8" height="6" fill="var(--mail)"/><path d="M0 0l4 3 4-3" stroke="var(--poster)" fill="none"/></svg>
      kate.anne.telford@mailbox-demo.com
    </p>
    <p class="block contact contact-two">
      <svg width="8" height="6" viewBox="0 0 8 6" aria-hidden="true"><rect width="8" height="6" fill="var(--mail)"/><path d="M0 0l4 3 4-3" stroke="var(--poster)" fill="none"/></svg>
      mtelford@vantor-telford.com.au
    </p>
  </main>
</body>
</html>
```